Web Design Job: Facial Surgery Center (Valorin)--Web Design Needed

We need a web design for Valorin Facial Surgery. Valorin is in Chesterfield, MO (suburb of St. Louis), and is owned by a double board certified facial plastic surgeon and ENT. The website must feature a before and after photo book, a section for patient reviews, drop down menus that outline services offered (one for surgical procedures and one for office/nonsurgical procedures), and "About the Practice" section, a section to talk about the doctor and his staff, a "What's New" section, a section for information for out of town patients, as well as a link to the Medical Spa also owned by the doctor, as well as Facebook and Twitter. We are open to ideas regarding adding a "tour of the surgery center", featuring video footage of the state of the art facility, as well as other video options. We prefer soothing colors such as aquas and blues, light greys, chocolate browns, etc (does not have to follow the color scheme in the attached logo). We would like the design to be easy to digest and informative, but not "thick". It should be an upscale, classy design that will appeal to all age brackets, but especially middle-aged women, as that is the primary clientele.

Target Market(s)

Middle aged women are our most common client, however, younger patients, both male and female, will often visit the site for select procedures.

Industry/Entity Type

Medical

Number of Pages Required

5+ page

Font styles to use
Sans Serif

Colors
86cfc6
85cae6
cee9f5
cfeae6
edf8f6
85acd3
cfdfed

Requirements
Must have
• Before and after picture book, links to Facebook, Twitter and Instagram, a soothing, peaceful aesthetic, a page for reviews, as well as a link to reviews on Yelp or similar page.
Nice to have
• Drop down menus that include the surgical and nonsurgical procedures. Each surgical procedure could have it's own section that includes a before and after picture book.
Should not have
• Too many words!

```html
<!DOCTYPE html>
<html lang="en">
<head>
<meta charset="utf-8">
<title>Valorin Facial Surgery</title>
<link href="https://fonts.googleapis.com/css2?family=Open+Sans:wght@300;400;600&display=swap" rel="stylesheet">
<style>
:root{
  --teal:#86cfc6;
  --teal-dark:#6fbdb3;
  --teal-pale:#cfeae6;
  --mint:#edf8f6;
  --blue:#3f9bd3;
  --blue-soft:#85acd3;
  --sky:#cee9f5;
  --ink:#333a3d;
  --muted:#777f82;
  --line:#e2e6e7;
  --grey-bg:#f6f7f7;
  --white:#ffffff;
  --heart:#e0344a;
}
*{box-sizing:border-box;margin:0;padding:0}
html,body{width:1200px;height:4905px;overflow:hidden}
body{font-family:"Open Sans",Arial,sans-serif;color:var(--ink);background:var(--white);position:relative}
.abs{position:absolute}
.btn{position:absolute;display:flex;align-items:center;justify-content:center;border:1px solid #c9cfd1;border-radius:20px;background:var(--white);font-size:11px;color:var(--muted);width:100px;height:26px}

/* header */
.site-header{position:absolute;left:0;top:0;width:1200px;height:98px}
.brand{position:absolute;left:105px;top:30px;font-size:28px;font-weight:400;color:var(--blue)}
.phone{position:absolute;right:115px;top:38px;font-size:14px;color:var(--muted)}
.search-dot{position:absolute;right:78px;top:35px;width:26px;height:26px;border-radius:50%;background:#d5d9da}
.main-nav{position:absolute;left:0;top:98px;width:1200px;height:49px;background:var(--teal)}
.main-nav ul{list-style:none;display:flex;margin-left:98px;height:49px}
.main-nav li{color:var(--white);font-size:14px;padding:0 26px;display:flex;align-items:center}
.main-nav li.active{background:var(--teal-dark)}
.dropdown{position:absolute;left:212px;top:147px;width:164px;background:#3a3f41;z-index:5;padding:8px 0}
.dropdown div{font-size:11px;padding:14px 16px;color:#f2f2f2}

/* hero */
.hero{position:absolute;left:0;top:147px;width:1200px;height:451px;background:linear-gradient(90deg,#f1efee,#f6f6f6 60%,#eeeeee)}
.hero-photo{position:absolute;left:0;top:0;width:560px;height:451px;background:linear-gradient(100deg,#e7d3c6,#d9bcaa 45%,#eee9e6)}
.hero-kicker{position:absolute;left:600px;top:80px;width:460px;text-align:center;font-size:11px;color:var(--teal-dark);letter-spacing:2px}
.hero-kicker:before,.hero-kicker:after{content:"";display:inline-block;width:160px;height:1px;background:var(--teal);vertical-align:middle;margin:0 10px}
.hero-title{position:absolute;left:600px;top:118px;width:460px;text-align:center;font-size:40px;font-weight:300;color:var(--blue)}
.hero-text{position:absolute;left:600px;top:180px;width:460px;text-align:center;font-size:15px;line-height:20px;color:var(--ink)}
.hero-cta{position:absolute;left:706px;top:256px;width:240px;height:38px;border-radius:20px;background:var(--teal);color:var(--white);font-size:13px;display:flex;align-items:center;justify-content:center;gap:10px}
.hero-more{position:absolute;left:790px;top:316px;font-size:11px;color:var(--ink)}
.hero-dots{position:absolute;left:543px;top:390px;display:flex;gap:6px}
.hero-dots span{width:12px;height:12px;border-radius:50%;border:2px solid var(--blue-soft)}

/* practice */
.section-title{position:absolute;width:1200px;text-align:center;font-size:34px;font-weight:300;color:var(--blue)}
.practice-item{position:absolute;width:260px;text-align:center}
.practice-item .circle{width:190px;height:190px;border-radius:50%;margin:0 auto;border:5px solid #f3f3f3}
.practice-item h3{font-size:15px;font-weight:400;margin-top:22px;color:var(--ink);letter-spacing:1px}
.practice-item h3.hl{color:var(--blue)}
.practice-item p{font-size:13px;line-height:17px;margin-top:14px;width:200px;margin-left:30px}

/* promo */
.promo{position:absolute;left:0;top:1216px;width:1200px;height:223px;background:var(--teal)}
.promo h2{position:absolute;left:98px;top:56px;font-size:30px;font-weight:300;color:var(--white)}
.promo p{position:absolute;left:98px;top:104px;font-size:18px;color:var(--white)}
.promo-btn{position:absolute;left:860px;top:66px;width:242px;height:40px;border-radius:20px;background:var(--white);font-size:13px;color:var(--ink);display:flex;align-items:center;justify-content:center;gap:10px}

/* before/after */
.ba-card{position:absolute;top:1511px;width:356px;height:549px;border:1px solid var(--line);background:var(--white)}
.ba-card h3{text-align:center;font-size:18px;font-weight:600;color:var(--blue);margin-top:38px;letter-spacing:1px}
.ba-card .photo{position:absolute;left:18px;top:88px;width:320px;height:353px}
.ba-card p{position:absolute;left:40px;top:470px;width:276px;text-align:center;font-size:13px;line-height:18px}
.arrow-btn{position:absolute;top:1768px;width:28px;height:28px;border-radius:50%}

/* gallery */
.gallery{position:absolute;left:0;top:2207px;width:1200px;height:654px;background:var(--grey-bg)}
.gallery h2{position:absolute;left:98px;top:96px;font-size:28px;font-weight:400;color:var(--blue)}
.gallery p{position:absolute;left:98px;top:144px;width:165px;font-size:13px;line-height:18px}
.tile{position:absolute;width:257px;height:212px}

/* info cards */
.info-card{position:absolute;top:2943px;width:317px;height:412px;border:1px solid var(--line);background:var(--white)}
.info-card .photo{position:absolute;left:16px;top:17px;width:285px;height:222px}
.info-card h3{position:absolute;left:0;top:262px;width:317px;text-align:center;font-size:14px;font-weight:400}
.info-card p{position:absolute;left:40px;top:292px;width:237px;text-align:center;font-size:11px;line-height:15px;color:var(--muted)}

/* reviews */
.reviews{position:absolute;left:0;top:3450px;width:1200px;height:595px;background:var(--teal)}
.reviews-photo{position:absolute;left:0;top:0;width:360px;height:595px;background:linear-gradient(90deg,#d8c7bc,#c9b0a0 60%,rgba(134,207,198,0))}
.reviews h2{position:absolute;left:0;top:82px;width:1200px;text-align:center;font-size:30px;font-weight:300;color:var(--white);letter-spacing:1px}
.review-card{position:absolute;top:186px;width:295px;height:278px;background:var(--white);text-align:center}
.review-card .who{font-size:11px;color:var(--blue);margin-top:26px}
.review-card .hearts{margin-top:10px;display:flex;justify-content:center;gap:3px}
.review-card p{font-size:13px;line-height:18px;margin:22px 30px 0}
.review-card .quote{position:absolute;right:22px;bottom:18px;font-size:36px;font-weight:600;line-height:20px;color:var(--ink)}
.review-dots{position:absolute;left:576px;top:520px;display:flex;gap:8px}
.review-dots span{width:10px;height:10px;border-radius:50%;background:rgba(255,255,255,.6)}
.review-dots span.on{background:var(--white)}

/* tour */
.tour h2{position:absolute;left:98px;top:4158px;width:330px;font-size:30px;font-weight:400;line-height:36px;color:var(--blue)}
.tour p{position:absolute;left:98px;top:4240px;width:330px;font-size:14px;line-height:19px}
.social{position:absolute;top:4408px;width:36px;height:36px;border-radius:50%;border:1px solid #9aa2a5}
.video{position:absolute;left:497px;top:4159px;width:605px;height:380px;background:linear-gradient(180deg,#8fb7dd 0%,#b5cfe2 40%,#7a9a5a 75%,#5f7f45 100%)}

/* footer */
.site-footer{position:absolute;left:0;top:4627px;width:1200px;height:278px;background:#f1f2f2}
.footer-brand{position:absolute;left:0;top:46px;width:1200px;text-align:center;font-size:22px;font-weight:400;color:var(--blue)}
.footer-links{position:absolute;left:0;top:100px;width:1200px;text-align:center;font-size:12px}
.footer-legal{position:absolute;left:0;top:124px;width:1200px;text-align:center;font-size:12px}
</style>
</head>
<body>

<header class="site-header">
  <div class="brand">Valorin</div>
  <div class="phone">Call us : (555) 014-2290</div>
  <div class="search-dot"></div>
</header>

<nav class="main-nav">
  <ul>
    <li class="active">Home</li>
    <li>Facial Procedures</li>
    <li>Office/Nonsurgical Procedures</li>
    <li>Our Practice</li>
    <li>Contact us</li>
    <li>Photo Gallery</li>
  </ul>
</nav>
<div class="dropdown">
  <div>Facial Procedures Link 1</div>
  <div>Facial Procedures Link 2</div>
  <div>Facial Procedures Link 3</div>
  <div>Facial Procedures Link 4</div>
  <div>Facial Procedures Link 5</div>
</div>

<section class="hero">
  <div class="hero-photo" role="img" aria-label="Portrait photo of a woman with smooth skin"></div>
  <div class="hero-kicker">WELCOME TO</div>
  <h1 class="hero-title">Valorin Facial Surgery</h1>
  <p class="hero-text">Lorem ipsum dolor sit amet, consectetur elit, sed do ut et magna aliqua. Ut enim minim veniam quis nostrud</p>
  <div class="hero-cta">Call to Action Button
    <svg width="14" height="10" viewBox="0 0 14 10"><path d="M0 5h12M8 1l4 4-4 4" stroke="#fff" stroke-width="1.6" fill="none"/></svg></div>
  <div class="hero-more">● Learn More</div>
  <div class="hero-dots"><span></span><span></span><span></span></div>
</section>

<section class="practice">
  <h2 class="section-title" style="top:682px">Our Practice</h2>
  <div class="practice-item" style="left:210px;top:790px">
    <div class="circle" role="img" aria-label="Close-up of lips with treatment" style="background:radial-gradient(circle,#e8b8a8,#f4e6df)"></div>
    <h3 class="hl">LOREM IPSUM DOLOR</h3>
    <p>Lorem ipsum consectetur adipisicing elit, sed do</p>
  </div>
  <div class="practice-item" style="left:468px;top:790px">
    <div class="circle" role="img" aria-label="Hands giving a facial massage" style="background:radial-gradient(circle,#c98a63,#9c5a38)"></div>
    <h3>LOREM IPSUM DOLOR</h3>
    <p>Lorem ipsum consectetur adipisicing elit, sed do</p>
  </div>
  <div class="practice-item" style="left:714px;top:790px">
    <div class="circle" role="img" aria-label="Portrait of a woman with clear skin" style="background:radial-gradient(circle,#ecd9cf,#e4e6ea)"></div>
    <h3>LOREM IPSUM DOLOR</h3>
    <p>Lorem ipsum consectetur adipisicing elit, sed do</p>
  </div>
  <div class="btn" style="left:290px;top:1090px">Learn More</div>
  <div class="btn" style="left:548px;top:1090px">Learn More</div>
  <div class="btn" style="left:794px;top:1090px">Learn More</div>
</section>

<section class="promo">
  <h2>Up to 30% Off Customized Facial Plastic Surgery</h2>
  <p>Lorem ipsum consectetur adipisicing elit, sed do</p>
  <div class="promo-btn">Make an Appointment
    <svg width="14" height="10" viewBox="0 0 14 10"><path d="M0 5h12M8 1l4 4-4 4" stroke="#333" stroke-width="1.6" fill="none"/></svg></div>
</section>

<section class="before-after">
  <div class="ba-card" style="left:229px">
    <h3>BEFORE</h3>
    <div class="photo" role="img" aria-label="Older woman's face before treatment" style="background:linear-gradient(135deg,#d9b8a4,#c89d85 55%,#e9e4e2)"></div>
    <p>Nulla id mollis nissel dolor. Proin purus enim, laoreet et libero</p>
  </div>
  <div class="ba-card" style="left:592px">
    <h3>AFTER</h3>
    <div class="photo" role="img" aria-label="Same woman's face after treatment" style="background:linear-gradient(135deg,#e6c7b3,#d9ae92 55%,#efeae8)"></div>
    <p>Nulla id mollis nissel dolor. Proin purus enim, laoreet et libero</p>
  </div>
  <svg class="arrow-btn" style="left:97px" viewBox="0 0 28 28"><circle cx="14" cy="14" r="14" fill="#c4c9cb"/><path d="M16 9l-5 5 5 5" stroke="#fff" stroke-width="2" fill="none"/></svg>
  <svg class="arrow-btn" style="left:1072px" viewBox="0 0 28 28"><circle cx="14" cy="14" r="14" fill="#86cfc6"/><path d="M12 9l5 5-5 5" stroke="#fff" stroke-width="2" fill="none"/></svg>
  <div class="btn" style="left:549px;top:2093px">Learn More</div>
</section>

<section class="gallery">
  <h2>Photo Gallery</h2>
  <p>Lorem ipsum adipisicing elit sed do incididunt ut labore et dolore magna aliqua. Ut enim veniam laboris</p>
  <div class="btn" style="left:98px;top:264px">Learn More</div>
  <div class="tile" role="img" aria-label="Woman touching her face" style="left:330px;top:102px;background:linear-gradient(135deg,#f1f1f1,#dcc3b4)"></div>
  <div class="tile" role="img" aria-label="Woman receiving a skin treatment" style="left:588px;top:102px;background:linear-gradient(135deg,#c9a58f,#e7d6cb)"></div>
  <div class="tile" role="img" aria-label="Injection treatment with gloved hand" style="left:846px;top:102px;background:linear-gradient(135deg,#e8ddd6,#9fb9cf)"></div>
  <div class="tile" role="img" aria-label="Woman receiving an injection" style="left:330px;top:316px;background:linear-gradient(135deg,#bfd8e6,#e5cfc3)"></div>
  <div class="tile" role="img" aria-label="Woman with facial mapping marks" style="left:588px;top:316px;background:linear-gradient(135deg,#d5e6ee,#e3d0c4)"></div>
  <div class="tile" role="img" aria-label="Woman with hands framing her face" style="left:846px;top:316px;background:linear-gradient(135deg,#f0d3bd,#e6c3a8)"></div>
</section>

<section class="info">
  <div class="info-card" style="left:98px">
    <div class="photo" role="img" aria-label="Woman touching her cheek" style="background:linear-gradient(135deg,#f3e2d6,#d6ab8f)"></div>
    <h3>What's New</h3>
    <p>Lorem ipsum adipisicing elit do incididunt ut aliqua. Ut enim veniam labore</p>
    <div class="btn" style="left:108px;top:360px">Learn More</div>
  </div>
  <div class="info-card" style="left:441px">
    <div class="photo" role="img" aria-label="Patient receiving a facial injection" style="background:linear-gradient(135deg,#8fb6cf,#d9c6bb)"></div>
    <h3>Information for out of town patients</h3>
    <p>Lorem ipsum adipisicing elit do incididunt ut aliqua. Ut enim veniam labore</p>
    <div class="btn" style="left:108px;top:360px">Learn More</div>
  </div>
  <div class="info-card" style="left:785px">
    <div class="photo" role="img" aria-label="Doctor consulting with a patient" style="background:linear-gradient(135deg,#e9eef2,#b8cbd9)"></div>
    <h3>Talk about the doctor and his staff</h3>
    <p>Lorem ipsum adipisicing elit do incididunt ut aliqua. Ut enim veniam labore</p>
    <div class="btn" style="left:108px;top:360px">Learn More</div>
  </div>
</section>

<section class="reviews">
  <div class="reviews-photo" role="img" aria-label="Woman with facial markings and a gloved hand"></div>
  <h2>PATIENT REVIEWS</h2>
  <div class="review-card" style="left:294px">
    <div class="who">Anna R. - September 13, 2014</div>
    <div class="hearts">
      <svg width="60" height="11" viewBox="0 0 60 11"><g fill="#e0344a"><path id="h" d="M5.5 10L1 5.5A2.6 2.6 0 015.5 2a2.6 2.6 0 014.5 3.5z"/><use href="#h" x="12"/><use href="#h" x="24"/><use href="#h" x="36"/><use href="#h" x="48"/></g></svg>
    </div>
    <p>Lorem ipsum dolor sit amet, dipisicing, sed do eiusmod incididunt ut labore et magna Lorem ipsum dolor sit amet</p>
    <div class="quote">”</div>
  </div>
  <div class="review-card" style="left:612px">
    <div class="who">Anna R. - September 13, 2014</div>
    <div class="hearts">
      <svg width="60" height="11" viewBox="0 0 60 11"><g fill="#e0344a"><use href="#h"/><use href="#h" x="12"/><use href="#h" x="24"/><use href="#h" x="36"/><use href="#h" x="48"/></g></svg>
    </div>
    <p>Lorem ipsum dolor sit amet, dipisicing, sed do eiusmod incididunt ut labore et magna Lorem ipsum dolor sit amet</p>
    <div class="quote">”</div>
  </div>
  <div class="review-dots"><span class="on"></span><span></span><span></span></div>
</section>

<section class="tour">
  <h2>Tour of the surgery cente</h2>
  <p>Lorem ipsum adipiscing elit sed do labore dolore magna aliqua. Ut enim veniam laboris</p>
  <div class="btn" style="left:98px;top:4330px">Learn More</div>
  <svg class="social" style="left:98px" viewBox="0 0 36 36"><path d="M19.5 28v-9h3l.5-3.5h-3.5v-2c0-1 .3-1.7 1.8-1.7h1.8V8.7c-.3 0-1.4-.2-2.7-.2-2.7 0-4.5 1.6-4.5 4.6v2.4h-3V19h3v9z" fill="#555"/></svg>
  <svg class="social" style="left:144px" viewBox="0 0 36 36"><path d="M10 23c2 1.3 4 1.8 6 1.8 6 0 9.5-5 9.3-9.6l1.6-1.6-1.9.5 1.4-1.7-1.9.7a3.2 3.2 0 00-5.5 2.9c-2.7-.1-5-1.4-6.6-3.3-.9 1.6-.4 3.5 1 4.3l-1.4-.4c0 1.6 1.1 2.9 2.6 3.2l-1.4.1c.4 1.3 1.7 2.2 3 2.3-1.3 1-3 1.5-4.7 1.3z" fill="#555"/></svg>
  <svg class="social" style="left:190px" viewBox="0 0 36 36"><g fill="#555"><circle cx="12.5" cy="23.5" r="2"/><path d="M11 16.5v2.6a6.4 6.4 0 016.4 6.4H20a9 9 0 00-9-9z"/><path d="M11 11.5v2.6a11.4 11.4 0 0111.4 11.4H25a14 14 0 00-14-14z"/></g></svg>
  <div class="video" role="img" aria-label="Video still of the surgery center building"></div>
  <svg class="abs" style="left:756px;top:4306px" width="86" height="86" viewBox="0 0 86 86"><circle cx="43" cy="43" r="43" fill="rgba(255,255,255,.75)"/><path d="M34 27l26 16-26 16z" fill="#7f8a8e"/></svg>
</section>

<footer class="site-footer">
  <div class="footer-brand">Valorin</div>
  <div class="footer-links">Home &nbsp;·&nbsp; Facial Procedures &nbsp;·&nbsp; Office/Nonsurgical Procedures &nbsp;·&nbsp; Our Practice &nbsp;·&nbsp; Contact us &nbsp;·&nbsp; Photo Gallery</div>
  <div class="footer-legal">Terms &amp; Conditions &nbsp;·&nbsp; Privacy © All Rights Reserved, Valorin Facial Surgery</div>
</footer>

</body>
</html>
```